Verpackungen für ein Standbodenbeutel Doypack
Zielgruppe
Wir betreiben eine eigene Öl-Manufaktur und bieten ausschließlich natureine Speiseöle und Tierprodukte - Superfood pulver.
Aufgabenstellung
Es wird auf einen Standbodenbeutel Doypack (braun) gedruckt. Es handelt sich um das Produkt Bio Hagebuttenpulver
Es sollte Naturel aussehen , was auf dem Packung stehen sollte u.a.
Schonend gemahlen
100% Vegan
100% natürlich
Ohne Zusatzstoffe
Verzehrempfehlung : Täglich 2 Teelöffel Bio Hagebuttenpulver nach Wunsch einnehmen.
Nährwert Tabelle
Eine Vorlage wurde vom Standbeutel wurde hochgeladen, auch das Firmen Logo wurde hochgeladen.
Die Datei sollteals Adobe Ai und ID
Bei Rückfragen einfach anschfreiben.

```html
<!DOCTYPE html>
<html lang="de">
<head>
<meta charset="utf-8">
<title>Bio Hagebuttenpulver – Standbodenbeutel</title>
<link href="https://fonts.googleapis.com/css2?family=Amatic+SC:wght@700&family=Alegreya+Sans:ital,wght@0,500;0,700;1,500;1,700&display=swap" rel="stylesheet">
<style>
  :root {
    --bg: #ffffff;
    --kraft: #c9a77d;
    --kraft-light: #d3b48c;
    --kraft-dark: #bd9a6f;
    --seal: #a98c68;
    --label: #050505;
    --olive: #789a2c;
    --teal: #2c7a66;
    --bio-bg: #6f9436;
    --bio-text: #e9dcb0;
    --table-text: #8c9a55;
    --rule: #4e6a22;
    --photo-green: #3e6f2a;
    --photo-red: #a8402c;
  }
  * { margin: 0; padding: 0; box-sizing: border-box; }
  html, body { width: 1200px; height: 1200px; overflow: hidden; background: var(--bg); }
  body { position: relative; font-family: "Alegreya Sans", sans-serif; }

  .pouch {
    position: absolute; top: 250px; width: 520px; height: 700px;
    background: linear-gradient(160deg, var(--kraft-light), var(--kraft) 50%, var(--kraft-dark));
  }
  .pouch--front { left: 40px; }
  .pouch--back { left: 640px; }
  .seal-line { position: absolute; left: 0; right: 0; height: 1px; background: var(--seal); opacity: .7; }
  .seal-line--upper { top: 62px; }
  .seal-line--lower { top: 84px; }

  .label { position: absolute; background: var(--label); text-align: center; }
  .pouch--front .label { left: 89px; top: 124px; width: 337px; height: 477px; }
  .pouch--back .label { left: 160px; top: 124px; width: 202px; height: 477px; }

  .brand { display: flex; flex-direction: column; align-items: center; gap: 6px; }
  .brand__dot { width: 18px; height: 18px; border-radius: 50%; background: var(--olive); }
  .brand__name { font-weight: 700; font-style: italic; color: var(--teal); font-size: 24px; }

  .bio-badge {
    display: inline-block; background: var(--bio-bg); color: var(--bio-text);
    border-radius: 50%; font-weight: 500;
  }
  .title {
    font-family: "Amatic SC", sans-serif; font-weight: 700; color: var(--olive);
    line-height: .85; letter-spacing: 1px;
  }
  .photo {
    margin: 0 auto;
    background: linear-gradient(90deg, var(--photo-green), var(--photo-red) 55%, var(--photo-green));
    opacity: .85;
  }
  .claims { color: var(--olive); font-weight: 700; line-height: 1.25; }
  .claims em { font-style: italic; }

  /* front */
  .pouch--front .brand { padding-top: 22px; }
  .pouch--front .bio-badge { margin-top: 48px; font-size: 28px; padding: 4px 22px; }
  .pouch--front .title { font-size: 74px; margin-top: 2px; }
  .pouch--front .photo { width: 240px; height: 110px; margin-top: 6px; }
  .pouch--front .claims { margin-top: 18px; font-size: 14px; padding-left: 60px; text-align: left; }
  .pouch--front .claims em { font-size: 15px; display: block; margin-left: -26px; }

  /* back */
  .pouch--back .frame-rule { position: absolute; top: 22px; bottom: 16px; width: 1px; background: var(--rule); }
  .pouch--back .frame-rule--left { left: 10px; }
  .pouch--back .frame-rule--right { right: 10px; }
  .pouch--back .bio-badge { margin-top: 22px; font-size: 15px; padding: 2px 10px; }
  .pouch--back .title { font-size: 38px; margin-top: 4px; }
  .pouch--back .claims { font-size: 12px; margin-top: 14px; font-weight: 500; }
  .pouch--back .claims em { font-weight: 500; }
  .pouch--back .photo { width: 150px; height: 70px; margin-top: 16px; }
  .usage { color: var(--teal); font-size: 9px; font-weight: 700; text-align: left; margin: 26px 24px 0; line-height: 1.2; }
  .nutrition { margin: 10px 24px 0; color: var(--table-text); font-size: 5.5px; text-align: left; }
  .nutrition__head { font-weight: 700; margin-bottom: 3px; line-height: 1.2; }
  .nutrition table { width: 100%; border-collapse: collapse; }
  .nutrition td { border-bottom: 0.5px solid var(--rule); padding: 0.6px 0; line-height: 1.15; vertical-align: bottom; }
  .nutrition td.value { text-align: right; white-space: nowrap; padding-left: 6px; }
  .pouch--back .brand { position: absolute; left: 0; right: 0; bottom: 24px; gap: 4px; }
  .pouch--back .brand__dot { width: 12px; height: 12px; }
  .pouch--back .brand__name { font-size: 16px; }
</style>
</head>
<body>
  <section class="pouch pouch--front">
    <div class="seal-line seal-line--upper"></div>
    <div class="seal-line seal-line--lower"></div>
    <div class="label">
      <div class="brand"><span class="brand__dot"></span><span class="brand__name">Kernwald</span></div>
      <span class="bio-badge">BIO</span>
      <h1 class="title">Hagebutten<br>Pulver</h1>
      <div class="photo" role="img" aria-label="Foto: drei rote Hagebutten mit grünen Blättern"></div>
      <p class="claims">schonend gemalen – Ohne Zusatzstoffe<em>100% Vegan – 100% natürlich</em></p>
    </div>
  </section>

  <section class="pouch pouch--back">
    <div class="seal-line seal-line--upper"></div>
    <div class="seal-line seal-line--lower"></div>
    <div class="label">
      <span class="frame-rule frame-rule--left"></span>
      <span class="frame-rule frame-rule--right"></span>
      <span class="bio-badge">BIO</span>
      <h2 class="title">Hagebutten<br>Pulver</h2>
      <p class="claims">schonend gemalen<br>ohne Zusatzstoffe<br><em>100% Vegan – 100% natürlich</em></p>
      <div class="photo" role="img" aria-label="Foto: drei rote Hagebutten mit grünen Blättern"></div>
      <p class="usage">Verzehrempfehlung:<br>Täglich 2 Teelöffel Bio Hagebuttenpulver<br>nach Wunsch einnehmen.</p>
      <div class="nutrition">
        <p class="nutrition__head">Durchschnittliche Nährwerte / Average nutritional value /<br>Valore nutrizionale medi a100g</p>
        <table>
          <tr><td>Energie/Energy/Energia</td><td class="value">0000 kJ/000 kcal</td></tr>
          <tr><td>Fett/Fat/Grassi</td><td class="value">00 g</td></tr>
          <tr><td>davon gesättigte Fettsäuren/of which<br>saturated fatty acids/di cui acidi grassi saturi</td><td class="value">00 g</td></tr>
          <tr><td>Kohlenhydrate/Carbohydrates/Carboidrati</td><td class="value">00 g</td></tr>
          <tr><td>davon Zucker/of which sugars/di cui zuccheri</td><td class="value">00 g</td></tr>
          <tr><td>Ballaststoffe/Dietary fibre/Fibre dietetica</td><td class="value">0,0 g</td></tr>
          <tr><td>Eiweiß/Protein/Proteine</td><td class="value">0 g</td></tr>
        </table>
      </div>
      <div class="brand"><span class="brand__dot"></span><span class="brand__name">Kernwald</span></div>
    </div>
  </section>
</body>
</html>
```